Business card design needed

am looking for a fun and funky design to match our moto, seriously fun swimwear and fashion for girls.

We manufacture and retail girls swimwear and fashion in Australia. Our designs are fun loving and funky. I would like to use bright fuschia to match our website www.breezyplum.com.au. We target a higher end market so need it to reflect this.

Industry/Entity Type

Fashion

Contact Information for Business Card

Breezy Plum logo,
Maddie Lorne
(07) 35517204
admin@breezyplum.com.au
www.breezyplum.com.au

Logo Text

Breezy Plum

```html
<!DOCTYPE html>
<html lang="en">
<head>
<meta charset="utf-8">
<title>Breezy Plum — Business Card</title>
<link rel="stylesheet" href="https://fonts.googleapis.com/css2?family=Special+Elite&family=Crimson+Text:wght@400&display=swap">
<style>
  :root {
    --fuchsia: #e5428f;
    --fuchsia-text: #e0388a;
    --paper: #f7f6f4;
    --stage: #e4e4e6;
    --rule: #c9c9c9;
    --white: #ffffff;
  }
  * { box-sizing: border-box; margin: 0; padding: 0; }
  html, body { width: 1200px; height: 1000px; overflow: hidden; }
  body {
    background: var(--stage);
    display: flex;
    align-items: center;
    justify-content: center;
  }
  .business-card {
    position: relative;
    width: 960px;
    height: 560px;
    background: var(--paper);
    overflow: hidden;
    box-shadow: 0 10px 30px rgba(0,0,0,0.18);
  }
  .brand {
    position: absolute;
    left: 64px;
    top: 46px;
    display: flex;
    align-items: center;
    gap: 14px;
  }
  .brand-dot {
    width: 34px;
    height: 34px;
    border-radius: 50%;
    background: var(--fuchsia);
  }
  .brand-name {
    font-family: "Crimson Text", serif;
    font-size: 40px;
    color: var(--fuchsia-text);
  }
  .contact-list {
    position: absolute;
    left: 110px;
    top: 124px;
    width: 460px;
    list-style: none;
  }
  .contact-list li {
    font-family: "Crimson Text", serif;
    font-size: 21px;
    color: var(--fuchsia-text);
    padding: 6px 0 4px;
    border-bottom: 2px dotted var(--rule);
    white-space: nowrap;
  }
  .name-badge {
    position: absolute;
    left: 660px;
    top: -40px;
    width: 580px;
    height: 580px;
    border-radius: 50%;
    background: var(--fuchsia);
  }
  .name-badge::after {
    content: "";
    position: absolute;
    inset: 16px;
    border-radius: 50%;
    border: 2px dashed rgba(255,255,255,0.75);
  }
  .holder {
    position: absolute;
    left: 730px;
    top: 196px;
    color: var(--white);
  }
  .holder-name {
    font-family: "Special Elite", monospace;
    font-size: 34px;
    letter-spacing: 6px;
    text-transform: uppercase;
  }
  .holder-role {
    font-family: "Crimson Text", serif;
    font-size: 26px;
    margin-top: 4px;
    margin-left: -14px;
  }
  .tagline-band {
    position: absolute;
    left: 0;
    right: 0;
    bottom: 0;
    height: 46px;
    background: var(--fuchsia);
    display: flex;
    align-items: center;
    padding-left: 24px;
    font-family: "Special Elite", monospace;
    font-size: 15.5px;
    letter-spacing: 1.5px;
    font-variant: small-caps;
    color: var(--white);
    white-space: nowrap;
  }
</style>
</head>
<body>
  <article class="business-card">
    <div class="brand">
      <span class="brand-dot"></span>
      <span class="brand-name">Breezy Plum</span>
    </div>

    <ul class="contact-list">
      <li>Postal Address: Po Box 4183, Birch Vale Q 4209</li>
      <li>Email: admin@breezyplum.com.au</li>
      <li>Phone: (07) 35517204</li>
      <li>Website: www.breezyplum.com.au</li>
      <li>Facebook: http://fb.com/breezyplumaustralia</li>
    </ul>

    <div class="name-badge"></div>
    <div class="holder">
      <p class="holder-name">Maddie Lorne</p>
      <p class="holder-role">General Maneger</p>
    </div>

    <p class="tagline-band">Breezy Plum is a boutique brand of 100% Australian made adorable, funky and fashionable swimwear for girls</p>
  </article>
</body>
</html>
```